Sassy Funky Web Design Project

NOTE: PAYMENT IS GUARANTEED for this project :)

++++++++++++++++++

I meant to share with you my mission for Caring Summit:

To inspire nurses to take action that impacts change in their lives, their organizations, or even the world.

Values:
I – Integrity
M – Mentoring / Motivation
P – Passion for excellence
A – Accountability
C – Competence / knowledge/ achievement
T – Transformation – positive change

++++++++++++++++++

This is a Membership site so will need to show 'Members Login' etc.

Please make sure you use SUPER HIGH QUALITY PHOTOGRAPHY / IMAGES :)

This is a WORDPRESS site for my client - here's some questions I asked her with her answers:

1. Why do you want a website (or have your current site redesigned)?

I want a website to generate income, and residual income, promote quality education material to professionals that is not the same on-line programs point and click to answer questions. I want an interactive way to make a impact in nursing hence CaringSUMMIT.

2. What’s your business/organization all about?

My parent company is Verity Brook Partners, LLC. I started it in 2001 and I provide consultative services to the legal and medical professionals. Mostly legal professionals; attorneys, and offer expert witness testimony. I also present full-day seminars regarding legal aspects of healthcare for nurses and hospital executive leaders. I am always promoting the professionalism in nursing where ever I can.

3. What sets your business apart from your competition?

What I will offer is instant access to quality and reliable clinical information and reliable business support for legal nurse consultants. I have not found another website that offers videos of clinical skills that nurses can watch over and over again without paying a lot of money for. Most of the information for nurses is through online learning read a packet, answer questions, and hopefully, maybe, they learned something. One of the reasons why my seminars are so well attended is they are interactive, and I use real examples to act out scenarios. I want nurses to be able to access short 7-10 minute video/podcasts that will show them how things are done and not just reading about it. Assessment skills will be performed on my family members in a clinic setting to create a realistic view. I want these to be somehow interactive if possible to reinforce the learning. Maybe you have some ideas on that.

For the legal nurse consultants. The programs are driving the “certification” outcome. When the nurses complete these programs, they have no experience and therefore are not able to recover their investment. I want to provide for them the same type of visual education support as the clinical nurses. These two audiences do not have to be mutually exclusive because they do tend to overlap in the real world.

I provide personal mentoring for novice legal nurse consultants in one week programs to support the application need in the LNC community. These weeks are valuable to the novice LNC trying to get started.

4. What problems does your business solve?

Application of concepts which is where I came up with Verity Brook Partners. I also have a tag with CaringSUMMIT I have used: Education, training, application. I put the theory into practice. I translate the pages to the living people.

5. Who are your prospective customers or visitors?

Customers:
Nurses, Advanced Practice Nurses, Legal Nurse Consultants, Attorneys for the clinical/medical information, Universities that offer nursing programs,
Nursing students (I really want to pursue this niche, perhaps a discount for enrolled students???)

Visitors:
Hospital Chief Nursing Officers, Attorneys, Long Term Care Administrators, Faculty of Nursing programs.

6. What do you NOT want on your website?

A flat appearing, boxy, traditional site. I want the nurses to be able to navigate through without much effort, remember many are technologically challenged….
NOooo cartoons… not too many stock photos, I would rather take real images if at all possible to keep the site “alive and real”.

What do you like?

QRV.tv: the listing of videos is going to be important in my site because I will be making clinical example videos and interview videos that can be viewed over and over again by the Platinum members. I plan to have a blog and many downloads available as well.

Tovamesh.com: I like the layout but I do want more interaction with mine. I do like the are you a training leader? Department leader: emerging leader? Componenets because I am addressing Nurses, Nurse Leaders, Legal Nurse Consultants… this would be important to establish right up front. I particularly like the video enhanced special report the new prospect has access to. I will do this for my site. I think it is also cool that you can change the color of the landing page to your liking.

www.thebrindlecove.com: I like a lot of things on this website but it is a bit difficult to navigate for even me. I like the short one minute capture of audio cds. I do plan to have CD material available. I do like the what you get with each level of membership under brindlelink tab. Some of the pages are not easy to read because the color is too dark and the font color is not contrasted enough. I like the tips in ten downloads on CD as well. I can see this working with mine as similar formatting with of course difference content.

www.ginaforsby.org: I do like the section she has on photo gallery where I can post event that have taken place as I speak, and work one-on-one with nurses across the country. (not the fashion shoot ?).

www.7horizons.com: I love the rollover interaction, the eyes constantly moving to the movement across the site.
http://www.dorvesta.org/DorvestaMultimedia.aspx?VideoId=8830461729004&type=M Quick lane video using sketchpad is a cool idea.

www.pebblevault.com - nice and clean

11. Please give us a list of websites that you DON’T Like and Why you Don’t like them.

www.lurn.com: landing page is way too crowded, too many colors, I don’t know where to go for what I would be looking for. Font is too small with large amounts of content.

www.casewardhub.com: this site is way too busy and difficult to navigate however I do like the page titled: Memorable BRWP cases. I would use a page like this for memorable Caring Summit experiences that would encourage others and remember the great things nurses do.

www.wardskills.com: Do not like at all. Way to juvenile.

Colour Scheme:

The colors palette I like is…. I think you will get the general idea of the color scheme. I like the yellow on dark colors so it pops, make sense?

F7C40E
4819A9
2E1FAC
F7D80E
Updates

Payment is guaranteed for this project now! :)

Thank you

Target Market(s)

Customers: Nurses, Advanced Practice Nurses, Legal Nurse Consultants, Attorneys for the clinical/medical information, Universities that offer nursing

Values:
I – Integrity
A – Accountability

Industry/Entity Type

Healthcare

Requirements
Must have
• professional, clean, VERY HIGH QUALITY IMAGES/ PHOTOGRAPHY e.g. PixQuarry
Nice to have
• Brock:
I have shown the design template to several people to get their first impression. I was shocked. They thought of the Tacoma Riveters! The football team. Ouch. I don’t want that. Crazy what others see.
Can we please change the color scheme to incorporate the colors below with the same layout. The Layout is good, it is the color I need to work a bit more on. Sorry about this but I don’t want to be a Riveters fan.

336699
FFCC66
FFFFFF
003366

Yvonne

New logo required: Caring Summit - DO NOT USE MEDICAL
Should not have
• childish graphics, or icons.
Don't want to see unprofessional site with clumsy type or template type designs. We can include some photos.

```html
<!DOCTYPE html>
<html lang="en">
<head>
<meta charset="utf-8">
<title>Caring Summit – Profile</title>
<link href="https://fonts.googleapis.com/css2?family=Signika:wght@300;400;600&family=PT+Sans:ital,wght@0,400;0,700;1,400&family=Open+Sans:wght@400;600;700&display=swap" rel="stylesheet">
<style>
:root{
  --navy:#003366;
  --blue:#336699;
  --gold:#ffcc66;
  --white:#ffffff;
  --ink:#3a3a3a;
  --muted:#555a60;
  --heading:#1d4e7e;
  --brand-ink:#4a4a4a;
  --page:#ffffff;
}
*{box-sizing:border-box;margin:0;padding:0}
html,body{width:986px;height:1200px;overflow:hidden;background:var(--page)}
body{position:relative;font-family:"PT Sans",sans-serif;color:var(--ink)}
.top-strip{position:absolute;left:0;top:0;width:986px;height:5px;background:#2e2e2e}

.brand{position:absolute;left:32px;top:52px;font-family:"Signika",sans-serif;font-weight:400;font-size:27px;line-height:1;color:var(--brand-ink)}

.utility{position:absolute;right:38px;top:15px;font-family:"Open Sans",sans-serif;font-size:12px;color:#333}
.utility a{color:#333;text-decoration:none}
.utility span{margin:0 7px;color:#777}

.search{position:absolute;left:714px;top:77px;width:236px;height:30px;border-radius:4px;background:var(--gold);border:1px solid #e7b04a;display:flex;align-items:center;justify-content:space-between;padding:0 8px 0 10px}
.search-label{font-family:"Signika",sans-serif;font-weight:300;font-style:italic;font-size:13px;color:#555}

.nav{position:absolute;left:0;top:128px;width:986px;height:46px;background:linear-gradient(#336699,#184a7c 55%,#003366);display:flex;padding-left:30px}
.nav a{font-family:"Signika",sans-serif;font-weight:300;font-size:16px;color:var(--white);text-decoration:none;padding:0 17px;line-height:46px;border-right:1px solid rgba(255,255,255,.75)}
.nav a:first-child{padding-left:17px}
.nav a:last-child{border-right:0}

.content{position:absolute;left:32px;top:200px;width:738px}
.section-title{display:flex;align-items:center;gap:6px;font-family:"Signika",sans-serif;font-weight:400;color:var(--heading)}
.section-title.major{font-size:19px;margin-bottom:20px}
.section-title.minor{font-size:14.5px;margin:33px 0 15px}
.content p{font-size:11.3px;line-height:17.1px;color:var(--muted);text-align:justify;margin-bottom:17.1px}
.content p.note{font-style:italic}
.more{display:block;margin:-1px 6px 0 auto;width:80px;height:25px;border-radius:4px;background:var(--gold);font-family:"Open Sans",sans-serif;font-weight:600;font-size:10px;color:#333;text-align:center;line-height:25px;letter-spacing:.3px;text-decoration:none}

.portrait{position:absolute;left:787px;top:210px;width:157px;height:216px;background:linear-gradient(160deg,#3b3230,#6b4a3a 45%,#a07c5e 75%,#2c2624)}

.footer{position:absolute;left:0;top:921px;width:986px;height:279px;background:linear-gradient(#3b6da0,#1c4d82 50%,#0c3868)}
.col{position:absolute;top:16px;font-family:"Open Sans",sans-serif;color:var(--white)}
.col h3{font-family:"Signika",sans-serif;font-weight:400;font-size:15.5px;margin-bottom:16px}
.col a{display:block;color:var(--white);text-decoration:none;font-size:11px;font-weight:600;line-height:24px}

.newsletter{position:absolute;left:571px;top:40px;width:373px;height:146px;border-radius:4px;overflow:hidden;background:#e8e8e8}
.nl-head{background:var(--gold);height:32px;padding:0 8px;font-family:"Signika",sans-serif;font-weight:400;font-size:12px;color:#222;line-height:32px}
.nl-body{padding:5px 8px 0;font-family:"Signika",sans-serif;font-weight:400;font-size:11.8px;line-height:22px;color:#333}
.nl-form{display:flex;align-items:center;justify-content:space-between;margin-top:6px}
.nl-input{width:240px;height:26px;border:1px solid #a9a9a9;border-radius:3px;background:#f2f2f2;font-size:10px;color:#999;padding-left:9px;line-height:24px;font-family:"Signika",sans-serif;font-weight:300}
.nl-submit{width:78px;height:25px;border-radius:3px;background:var(--blue);color:var(--white);font-family:"Signika",sans-serif;font-weight:400;font-size:14px;text-align:center;line-height:25px;margin-right:10px}
.nl-foot{position:absolute;left:0;bottom:0;width:100%;height:24px;background:var(--gold);padding-left:11px;font-family:"Signika",sans-serif;font-weight:400;font-size:11.8px;line-height:24px;color:#222}

.social{position:absolute;left:806px;top:201px;display:flex;gap:5px}
.social span{width:38px;height:38px;border-radius:50%;background:#f4f4f4;border:1px solid #cfd6de}

.rule{position:absolute;left:29px;top:247px;width:921px;height:1px;background:rgba(255,255,255,.35)}
.copyright{position:absolute;left:31px;top:256px;font-family:"Open Sans",sans-serif;font-weight:600;font-size:11px;color:var(--white)}
</style>
</head>
<body>
<div class="top-strip"></div>

<header>
  <div class="brand">Caring Summit</div>

  <nav class="utility"><a href="#">Member Login</a><span>|</span><a href="#">Client</a><span>|</span><a href="#">Support</a><span>|</span><a href="#">FAQ</a></nav>

  <div class="search">
    <span class="search-label">Search here</span>
    <svg width="20" height="18" viewBox="0 0 20 18" aria-hidden="true"><circle cx="8" cy="7.5" r="5.8" fill="none" stroke="#111" stroke-width="2.2"/><line x1="12.3" y1="11.5" x2="18" y2="16.5" stroke="#111" stroke-width="3" stroke-linecap="round"/></svg>
  </div>
</header>

<nav class="nav">
  <a href="#">Main</a><a href="#">About Company</a><a href="#">Services</a><a href="#">Seminars</a><a href="#">Blog</a><a href="#">Member Login</a><a href="#">Contact Us</a>
</nav>

<main class="content">
  <h1 class="section-title major">
    <svg width="36" height="36" viewBox="0 0 36 36" aria-hidden="true"><path d="M3 10 Q12 2 20 8 Q26 3 33 5" fill="none" stroke="#1d4e7e" stroke-width="2.4"/><path d="M3 10 Q4 26 16 33" fill="none" stroke="#1d4e7e" stroke-width="2.4"/></svg>
    Profile
  </h1>
  <p>Lorem Ipsum is simply dummy text of the printing and typesetting industry. Lorem Ipsum has been the industry's standard dummy text ever since the 1500s, when an unknown printer took a galley of type and scrambled it to make a type specimen book. It has survived not only five centuries, but also the leap into electronic typesetting, remaining essentially unchanged.</p>
  <p class="note">It was popularised in the 1960s with the release of Typemark sheets containing Lorem Ipsum passages, and more recently with desktop publishing software like Quillset PageWorks including version.</p>
  <p>Contrary to popular belief, Lorem Ipsum is not simply random text. It has roots in a piece of classical Latin literature from 45 BC, making it over 2000 years old. Walter Pemberley, a Latin professor at Ashgrove College in Virginia, looked up one of the more obscure Latin words, consectetur, from a Lorem Ipsum passage, and going through the cites of the word in classical literature, discovered the undoubtable source. Lorem Ipsum comes from sections 1.10.32 and 1.10.33 of "de Finibus Bonorum et Malorum" (The Extremes of Good and Evil) by Varrenus, written in 45 BC. This book is a treatise on the theory of ethics, very popular during the Renaissance. The first line of Lorem Ipsum, "Lorem ipsum dolor sit amet..", comes from a line in section 1.10.32.</p>
  <p class="note">The standard chunk of Lorem Ipsum used since the 1500s is reproduced below for those interested. Sections 1.10.32 and 1.10.33 from "de Finibus Bonorum et Malorum" by Varrenus are also reproduced in their exact original form, accompanied by English versions from the 1914 translation by J. Holloway.</p>

  <h2 class="section-title minor">
    <svg width="21" height="16" viewBox="0 0 21 16" aria-hidden="true"><path d="M1 1 L8 8 L1 15 M10 1 L17 8 L10 15" fill="none" stroke="#1d5fa0" stroke-width="3.2"/></svg>
    Sub Heading
  </h2>
  <p>Lorem Ipsum is simply dummy text of the printing and typesetting industry. Lorem Ipsum has been the industry's standard dummy text ever since the 1500s, when an unknown printer took a galley of type and scrambled it to make a type specimen book. It has survived not only five centuries, but also the leap into electronic typesetting, remaining essentially unchanged.</p>
  <p class="note">It was popularised in the 1960s with the release of Typemark sheets containing Lorem Ipsum passages, and more recently with desktop publishing software like Quillset PageWorks including version.</p>
  <p>Contrary to popular belief, Lorem Ipsum is not simply random text. It has roots in a piece of classical Latin literature from 45 BC, making it over 2000 years old. Walter Pemberley, a Latin professor at Ashgrove College in Virginia, looked up one of the more obscure Latin words, consectetur, from a Lorem Ipsum passage, and going through the cites of the word in classical literature, discovered the undoubtable source. Lorem Ipsum comes from sections 1.10.32 and 1.10.33 of "de Finibus Bonorum et Malorum" (The Extremes of Good and Evil) by Varrenus, written in 45 BC. This book is a treatise on the theory of ethics, very popular during the Renaissance. The first line of Lorem Ipsum, "Lorem ipsum dolor sit amet..", comes from a line in section 1.10.32.</p>
  <p class="note">The standard chunk of Lorem Ipsum used since the 1500s is reproduced below for those interested. Sections 1.10.32 and 1.10.33 from "de Finibus Bonorum et Malorum" by Varrenus are also reproduced in their exact original form, accompanied by English versions from the 1914 translation by J. Holloway.</p>
  <a class="more" href="#">VIEW MORE</a>
</main>

<div class="portrait" role="img" aria-label="Portrait photograph of the founder"></div>

<footer class="footer">
  <div class="col" style="left:30px"><h3>Company</h3><a href="#">Company</a><a href="#">Media Resources</a><a href="#">Press Releases</a><a href="#">News</a><a href="#">Contact</a></div>
  <div class="col" style="left:170px;top:17px"><h3>Why We Are</h3><a href="#">Why Choose Us</a><a href="#">Testimonials</a><a href="#">Recent Blog</a><a href="#">Features</a></div>
  <div class="col" style="left:309px;top:18px"><h3>Services</h3><a href="#">Why Choose Us</a><a href="#">Testimonials</a><a href="#">Recent Blog</a><a href="#">Features</a></div>
  <div class="col" style="left:444px"><h3>Support &amp; FAQ</h3><a href="#">Support</a><a href="#">Blog</a><a href="#">Video</a><a href="#">Support</a></div>
  <div class="col" style="left:578px;top:15px"><h3>Newsletter</h3></div>

  <div class="newsletter">
    <div class="nl-head">Yvonne C Marlowe-Tenant: Expert Author Email Alerts</div>
    <div class="nl-body">
      Sign up to receive email alerts of Yvonne C Marlowe-Tenant's latest articles from ArticleHarbor.com!
      <div class="nl-form"><span class="nl-input">Enter your Email Address</span><span class="nl-submit">Submit</span></div>
    </div>
    <div class="nl-foot">Lorem ipsum.com</div>
  </div>

  <div class="social" aria-label="Social links"><span></span><span></span><span></span></div>
  <div class="rule"></div>
  <div class="copyright">© 2012 Company Name &nbsp;|&nbsp; All right reserved</div>
</footer>
</body>
</html>
```